Financial Services Flyer for Healthcare Providers

We need a flyer design for a product of Talvo Financial (www.talvofinancial.example) called the PLUM program. Attached you will find the content for the flyer. Please use your own creativity and keep in mind the this is a product of Talvo Financial, a financial services company that works in the field of healthcare. If you have any questions or comments, please feel free to ask....

Target Market(s)

Our target audience is healthcare providers.

Industry/Entity Type

Financial

Requirements
Must have
• Eye catching graphics and colors but still look fairly conservative since our audience is somewhat conservative.
Nice to have
• Nice looking, smiling, upbeat people in pictorial portions of the flyer.
Should not have
• Our clients are all found in America, so the look, feel and subtext should all target an American audience and not have the look and feel of being from outside of the US.

```html
<!DOCTYPE html>
<html lang="en">
<head>
<meta charset="utf-8">
<title>Talvo Financial – PLUM Program</title>
<link href="https://fonts.googleapis.com/css2?family=Cabin+Condensed:wght@400;500;600&family=Open+Sans:wght@400;600;700&display=swap" rel="stylesheet">
<style>
  :root {
    --brand-blue: #29a8e0;
    --slate: #6d6e71;
    --ink: #231f20;
    --maroon: #5a1a1c;
    --paper: #ffffff;
    --icon-grey: #77787b;
  }
  * { margin: 0; padding: 0; box-sizing: border-box; }
  html, body { width: 953px; height: 1200px; overflow: hidden; background: var(--paper); }
  .flyer {
    position: relative; width: 953px; height: 1200px; background: var(--paper);
    font-family: "Open Sans", Arial, sans-serif; color: var(--ink);
  }
  .header { position: absolute; left: 0; top: 0; width: 953px; height: 147px; }
  .brand { position: absolute; left: 36px; top: 50px; display: flex; align-items: center; gap: 14px; }
  .brand-mark { width: 42px; height: 42px; background: var(--maroon); border-radius: 6px; }
  .brand-name { font-family: "Open Sans", Arial, sans-serif; font-size: 50px; font-weight: 600; color: var(--slate); letter-spacing: -1px; line-height: 1; }
  .header-divider { position: absolute; left: 410px; top: 44px; width: 1px; height: 78px; background: #c9c9c9; }
  .tagline { position: absolute; left: 436px; top: 48px; font-size: 22px; line-height: 26px; letter-spacing: .5px; }
  .tagline span { display: block; }
  .tagline .t1 { color: var(--maroon); }
  .tagline .t2 { color: var(--ink); }
  .tagline .t3 { color: var(--slate); }

  .hero {
    position: absolute; left: 0; top: 147px; width: 953px; height: 508px;
    background: linear-gradient(100deg, #f4f6f7 0%, #e8eef1 30%, #dfe9ef 50%, #eef1f2 70%, #d9e1e6 100%);
  }
  .program-title { position: absolute; left: 34px; top: 517px; }
  .program-title .word-plum {
    display: block; width: 274px; height: 60px; background: var(--brand-blue); color: #fff;
    font-weight: 700; font-size: 50px; line-height: 60px; padding-left: 32px; letter-spacing: 1px;
  }
  .program-title .word-program {
    display: block; width: 348px; height: 59px; background: var(--slate); color: #fff;
    font-weight: 400; font-size: 40px; line-height: 59px; padding-left: 32px;
  }

  .section-heading { font-family: "Cabin Condensed", "Arial Narrow", sans-serif; font-weight: 500; color: var(--brand-blue); }
  .about { position: absolute; left: 33px; top: 708px; width: 398px; }
  .about .section-heading { font-size: 27px; line-height: 32px; margin-bottom: 14px; }
  .about p { margin-left: 4px; font-size: 16px; line-height: 23.5px; text-align: justify; margin-bottom: 4px; }
  .hl { color: var(--brand-blue); }
  .costs { position: absolute; left: 33px; top: 982px; width: 398px; }
  .costs .section-heading { font-size: 27px; line-height: 32px; margin-bottom: 12px; }
  .costs p { margin-left: 4px; font-size: 16px; line-height: 27px; }

  .how-panel {
    position: absolute; left: 530px; top: 687px; width: 423px; height: 415px;
    background: var(--brand-blue); border-radius: 22px 0 0 22px;
  }
  .how-panel .panel-title { position: absolute; left: 32px; top: 16px; font-family: "Cabin Condensed", "Arial Narrow", sans-serif; font-weight: 500; font-size: 27px; color: #fff; }
  .step { position: absolute; left: 53px; width: 350px; color: #fff; }
  .step h3 { font-family: "Cabin Condensed", "Arial Narrow", sans-serif; font-weight: 500; font-size: 18px; line-height: 22px; margin-bottom: 2px; }
  .step p { font-family: "Cabin Condensed", "Arial Narrow", sans-serif; font-size: 13.5px; line-height: 15.5px; }
  .step-1 { top: 80px; } .step-2 { top: 193px; } .step-3 { top: 306px; }
  .step-icon {
    position: absolute; left: 504px; width: 64px; height: 64px; border-radius: 50%;
    background: var(--icon-grey); border: 3px solid #fff; display: flex; align-items: center; justify-content: center;
  }
  .icon-1 { top: 762px; } .icon-2 { top: 878px; } .icon-3 { top: 992px; }

  .cta-band {
    position: absolute; left: 0; top: 1135px; width: 953px; height: 65px; background: var(--brand-blue);
    color: #fff; font-weight: 700; font-size: 30px; display: flex; align-items: center;
  }
  .cta-text { position: absolute; left: 155px; }
  .cta-phone-icon { position: absolute; left: 455px; top: 12px; }
  .cta-number { position: absolute; left: 527px; }
</style>
</head>
<body>
<div class="flyer">
  <header class="header">
    <div class="brand"><span class="brand-mark"></span><span class="brand-name">Talvo Financial</span></div>
    <div class="header-divider"></div>
    <div class="tagline"><span class="t1">Receivable</span><span class="t2">Management</span><span class="t3">Solutions</span></div>
  </header>

  <div class="hero" role="img" aria-label="Photo of a smiling team of doctors and nurses in white coats"></div>
  <div class="program-title"><span class="word-plum">PLUM</span><span class="word-program">PROGRAM</span></div>

  <section class="about">
    <h2 class="section-heading">Claims Evaluation &amp; Recovery Team</h2>
    <p>At Talvo financial, <span class="hl">PLUM</span> locates underpaid claims and turns write offs into added revenue.</p>
    <p><span class="hl">PLUM</span> uses a genius revenue cycle application that identifies potentially underpaid claims for hospitals. Once revenue has been located, our medical billers correct the claims and appeal to insurance for payment.</p>
  </section>

  <section class="costs">
    <h2 class="section-heading">Costs</h2>
    <p><span class="hl">PLUM</span> charges nothing unless it finds and collects lost revenue for you!</p>
  </section>

  <section class="how-panel">
    <h2 class="panel-title">How PLUM works</h2>
    <div class="step step-1"><h3>Remote Evaluation:</h3><p>With a secure and temporary login into any healthcare operating system a random account evaluation is conducted by a highly skilled revenue cycle auditor.</p></div>
    <div class="step step-2"><h3>Data Exchange:</h3><p>When missed revenue is found, a simple data exchange will be recommended. Through the exchange, PLUM will arrange to connect your claims data into the PLUM work flow.</p></div>
    <div class="step step-3"><h3>Collections:</h3><p>PLUM disperses underpaid claims to our medical billers for prompt recovery.</p></div>
  </section>

  <div class="step-icon icon-1">
    <svg width="36" height="36" viewBox="0 0 36 36" fill="none" stroke="#fff" stroke-width="4" stroke-linecap="round">
      <path d="M29 18a11 11 0 1 1-4-8.5"/><path d="M26 4v7h-7" stroke-linejoin="round"/>
    </svg>
  </div>
  <div class="step-icon icon-2">
    <svg width="40" height="36" viewBox="0 0 40 36" fill="#fff">
      <path d="M2 4h8l2 3h10v9H2z"/><path d="M18 20h8l2 3h10v10H18z"/>
      <path d="M27 6h6v6" fill="none" stroke="#fff" stroke-width="2"/><path d="M33 12l-3-3h6z"/>
      <path d="M12 32H6v-9" fill="none" stroke="#fff" stroke-width="2"/><path d="M6 20l-3 4h6z"/>
    </svg>
  </div>
  <div class="step-icon icon-3">
    <svg width="34" height="38" viewBox="0 0 34 38">
      <path d="M11 2h12l-4 7h-4z" fill="#fff"/>
      <path d="M13 10h8c8 6 12 13 11 19-1 6-6 8-15 8S2 35 2 29c-1-6 3-13 11-19z" fill="#fff"/>
      <circle cx="17" cy="25" r="8" fill="var(--icon-grey)"/>
      <text x="17" y="30" text-anchor="middle" font-family="Open Sans, sans-serif" font-weight="700" font-size="13" fill="#fff">$</text>
    </svg>
  </div>

  <footer class="cta-band">
    <span class="cta-text">GET PLUM TODAY!</span>
    <svg class="cta-phone-icon" width="40" height="40" viewBox="0 0 40 40" fill="none" stroke="#fff" stroke-width="2.5">
      <circle cx="20" cy="20" r="17"/>
      <path d="M14 11c-2 1-3 3-2 6 2 5 6 10 11 12 3 1 5 0 6-2l-3-4-3 1c-2-1-4-4-5-6l1-3z" fill="#fff" stroke="none"/>
      <path d="M23 11a7 7 0 0 1 6 6M23 7a11 11 0 0 1 10 10" stroke-width="2"/>
    </svg>
    <span class="cta-number">1-800-555-0142</span>
  </footer>
</div>
</body>
</html>
```